Lukas Brandstetter, systemic consultant.

Minimalism as a lifestyle means: conscious renunciation to make room for the essentials. My homepage should present itself easily and clearly. Just design in the colors of the logo, thanks. Insert my personal photos very discreetly. Clear headings that convey seriousness, clarity and confidence. As a systemic consultant, I usually coach clients virtually using video chat (zoom). Clear solutions and support are my core competence. My homepage should be sober and yet inviting and arouse curiosity. The focus is my consulting skills and my life experience! My services are honest, human and trustworthy. My homepage is not complicated, playful and chaotic. It is clear and clearly structured. Less is more!! My homepage should also have a podcast.

Target Market(s)

Highly sensitive people between 20-60, artists, actors, athletes, managers...

Industry/Entity Type

Coaching-Leading

Font styles to use
Serif

Requirements
Must have
• Clarity, openness, digital, structure, simple, seriousness, good feeling!!
Nice to have
• Big photos and pictures. Colors from the logo, only 3 pages hp would be optimal, a simple-simple homepage!
Should not have
• Colourful, complicated, nested, playful.

```html
<!DOCTYPE html>
<html lang="en">
<head>
<meta charset="utf-8">
<title>Lukas Brandstetter – Systemic Consultant</title>
<link href="https://fonts.googleapis.com/css2?family=Prata&family=Mulish:wght@400;600;700;800&display=swap" rel="stylesheet">
<style>
:root{
  --red:#b0102a;
  --ink:#1e1e1e;
  --ink-2:#262424;
  --ink-3:#3a3a3a;
  --text:#3b3b3b;
  --muted:#5e5e5e;
  --band:#f0eef1;
  --white:#ffffff;
}
*{margin:0;padding:0;box-sizing:border-box}
html,body{width:1200px;height:5133px;overflow:hidden}
body{position:relative;background:var(--white);font-family:"Mulish",Arial,sans-serif;color:var(--text)}
.serif{font-family:"Prata",Georgia,serif;font-weight:400}
section,header,footer{position:absolute;left:0;width:1200px}
.abs{position:absolute}
.photo{position:absolute}
.btn{position:absolute;display:flex;align-items:center;justify-content:center;border-radius:30px;font-weight:700;text-decoration:none}
.btn-outline{border:2px solid var(--red);color:var(--red);background:var(--white)}
.btn-white{background:var(--white);color:var(--ink);font-size:13px}
.btn-red{background:var(--red);color:var(--white)}

/* header */
.site-header{top:0;height:68px;background:var(--ink)}
.brand{position:absolute;left:128px;top:22px;color:var(--white);font-family:"Mulish",Arial,sans-serif;font-weight:700;font-size:19px;line-height:24px}
.main-nav{position:absolute;right:128px;top:24px;display:flex;gap:34px;font-size:14px;color:var(--white)}
.main-nav .active{color:var(--red);text-decoration:underline}

/* hero */
.hero{top:68px;height:646px;background:var(--white);box-shadow:0 4px 6px rgba(0,0,0,.06)}
.hero-portrait{left:120px;top:28px;width:500px;height:618px;border-radius:240px 240px 0 0;background:linear-gradient(180deg,#c7b1a2 0%,#8a7366 30%,#2a2a2a 55%,#161616 100%)}
.hero-title{left:650px;top:58px;font-size:64px;line-height:66px;color:var(--ink)}
.hero-text{left:656px;top:228px;width:390px;font-size:16px;line-height:22px;color:var(--text)}
.hero-btn{left:654px;top:308px;width:132px;height:44px;font-size:15px}
.hero-link{position:absolute;width:194px;height:24px;border-bottom:2px solid var(--ink);font-size:14px;color:var(--ink);display:flex;justify-content:space-between;align-items:flex-start}

/* guides */
.guides{top:714px;height:442px;background:var(--white)}
.guide{position:absolute;top:56px;width:228px;height:328px;border-radius:4px;padding:26px 28px;color:var(--white)}
.guide h3{font-family:"Prata",Georgia,serif;font-weight:400;font-size:20px;margin-bottom:18px}
.guide p{font-family:"Prata",Georgia,serif;font-size:15px;line-height:24px}
.guide .btn{left:28px;top:266px;width:94px;height:30px}
.g1{left:128px;background:var(--red)}
.g2{left:366px;background:var(--ink)}
.g3{left:604px;background:var(--ink-2)}
.g4{left:842px;background:var(--ink-3)}

/* about */
.about{top:1156px;height:528px;border-top:1px solid #eee;border-bottom:1px solid #e4e4e4}
.about-portrait{left:128px;top:58px;width:396px;height:396px;border-radius:50%;background:radial-gradient(circle at 50% 40%,#c9a999 0%,#8e7468 35%,#5a5a5a 65%,#3e3e3e 100%)}
.about-title{left:584px;top:52px;font-size:42px;color:var(--ink);border-bottom:2px solid var(--ink);line-height:54px}
.about-text{left:584px;top:146px;width:486px;font-size:14.5px;line-height:23px;text-align:justify}
.about-btn{left:584px;top:400px;width:132px;height:44px;font-size:15px}

/* services */
.services{top:1684px;height:674px}
.section-title{position:absolute;left:0;width:1200px;text-align:center;font-size:42px;color:var(--ink)}
.title-rule{position:absolute;left:564px;width:72px;height:2px;background:var(--ink)}
.service{position:absolute;top:162px;width:302px;text-align:center}
.service .photo{position:relative;width:302px;height:272px;border-radius:4px}
.service h3{font-family:"Prata",Georgia,serif;font-weight:400;font-size:20px;color:var(--ink);margin-top:26px}
.service p{font-size:12.5px;line-height:19px;color:var(--muted);margin:12px auto 0;width:270px}
.service .btn{position:relative;margin:22px auto 0;width:92px;height:32px;font-size:12px}

/* events */
.events{top:2358px;height:432px;background:var(--band)}
.event-box{position:absolute;left:128px;top:48px;width:940px;height:328px;border-radius:4px;overflow:hidden;display:flex}
.event-photo{width:234px;height:328px}
.event-info{width:236px;height:328px;padding:42px 24px;color:var(--white)}
.event-info h3{font-family:"Prata",Georgia,serif;font-weight:400;font-size:21px;line-height:29px}
.event-info h4{font-size:12px;font-weight:800;margin:30px 0 18px}
.event-info p{font-size:12.5px;line-height:22px}
.event-info .btn{position:relative;margin-top:26px;width:90px;height:30px;font-size:12px}

/* tiger */
.tiger{top:2790px;height:520px;background:#000}
.tiger-art{left:0;top:30px;width:600px;height:458px;background:radial-gradient(ellipse at 40% 45%,#9a9a9a 0%,#5c5c5c 35%,#222 65%,#000 85%)}
.tiger-rule{position:absolute;left:776px;width:112px;height:2px;background:var(--white)}
.tiger-title{position:absolute;left:560px;top:156px;width:544px;text-align:center;color:var(--white);font-size:54px;line-height:60px}

/* blog */
.blog{top:3278px;height:644px;background:#f7f6f8;border-top-right-radius:90px}
.blog-photo{left:132px;top:164px;width:494px;height:416px;border-radius:4px;background:linear-gradient(160deg,#e9e6e2 0%,#9aa5b3 40%,#2f4a78 62%,#262c36 100%)}
.post{position:absolute;left:662px;width:410px;padding:0 20px}
.post time{font-size:10px;color:var(--muted)}
.post h3{font-family:"Prata",Georgia,serif;font-weight:400;font-size:19px;color:var(--ink);margin:6px 0}
.post p{font-size:11.5px;line-height:17px;color:var(--muted)}
.post-rule{position:absolute;left:662px;width:410px;height:1px;background:#999}

/* advantage */
.advantage{top:3922px;height:512px;background:var(--white)}
.eyebrow{left:128px;top:86px;font-family:"Prata",Georgia,serif;font-size:18px;color:var(--ink);border-bottom:1px solid var(--ink)}
.adv-title{left:128px;top:130px;font-size:36px;line-height:44px;color:var(--ink)}
.adv-text{left:128px;top:290px;width:330px;font-size:12.5px;line-height:19px;color:var(--muted)}
.adv-btn{left:128px;top:390px;width:130px;height:44px;font-size:15px}
.adv-photo{top:60px;height:390px;border-radius:10px}

/* cta */
.cta{top:4434px;height:384px;background:linear-gradient(90deg,#1c1b1d 0%,#2b2a2d 50%,#1a191b 100%);text-align:center;color:var(--white)}
.cta h2{position:absolute;left:0;width:1200px;top:70px;font-size:36px;letter-spacing:.5px}
.cta p{position:absolute;left:200px;width:800px;top:134px;font-size:17px;line-height:26px}
.cta-btn{left:534px;top:214px;width:132px;height:44px;font-size:15px}

/* footer */
.site-footer{top:4818px;height:315px;background:var(--ink);color:var(--white)}
.footer-brand{position:absolute;left:0;width:1200px;top:74px;text-align:center;font-family:"Mulish",Arial,sans-serif;font-weight:700;font-size:19px;line-height:24px}
.footer-nav{position:absolute;left:0;width:1200px;top:138px;display:flex;justify-content:center;gap:30px;font-size:14px}
.follow{position:absolute;left:0;width:1200px;top:194px;display:flex;justify-content:center;align-items:center;gap:12px;font-size:13px}
.social{width:16px;height:16px;border-radius:50%;border:2px solid var(--white)}
.copy{position:absolute;left:0;width:1200px;top:260px;text-align:center;font-size:11px}
</style>
</head>
<body>

<header class="site-header">
  <div class="brand">Lukas Brandstetter</div>
  <nav class="main-nav">
    <span class="active">Home</span><span>About Us</span><span>Solutions</span><span>Courses &amp; Services</span><span>Events</span><span>Contact Us</span>
  </nav>
</header>

<section class="hero">
  <div class="photo hero-portrait" role="img" aria-label="Portrait of Lukas Brandstetter in a dark suit"></div>
  <h1 class="abs serif hero-title">Consultant<br>Coach Leader.</h1>
  <p class="abs hero-text">There are many variations of passages of Lorem Ipsum available, but the majority have.</p>
  <a class="btn btn-outline hero-btn">Read More</a>
  <div class="hero-link" style="left:652px;top:428px">Develop Your Leaders <span>›</span></div>
  <div class="hero-link" style="left:876px;top:428px">Engage Your People <span>›</span></div>
  <div class="hero-link" style="left:652px;top:532px">Build a Winning Culture <span>›</span></div>
  <div class="hero-link" style="left:876px;top:532px">Lorem Ipsum dummy <span>›</span></div>
</section>

<section class="guides">
  <div class="guide g1"><h3>Free Guide</h3><p>6 Ways to Help Your Team Handle Stress During Times of Change</p><a class="btn btn-white">Read More</a></div>
  <div class="guide g2"><h3>Free Guide</h3><p>There are many variations of passages of Lorem Ipsum available, but the majority have suffered.</p><a class="btn btn-white">Read More</a></div>
  <div class="guide g3"><h3>Free Guide</h3><p>On the other hand, we denounce with righteous indign ation and dislike men who are so beguiled</p><a class="btn btn-white">Read More</a></div>
  <div class="guide g4"><h3>Free Guide</h3><p>when our power of choice is untra mmelled and when nothing prevents our being able to do what we like.</p><a class="btn btn-white">Read More</a></div>
</section>

<section class="about">
  <div class="photo about-portrait" role="img" aria-label="Round portrait photo of Lukas Brandstetter"></div>
  <h2 class="abs serif about-title">About Me</h2>
  <p class="abs about-text">At vero eos et accusamus et iusto odio dignissimos ducimus qui blanditiis praesentium voluptatum deleniti atque corrupti quos dolores et quas molestias excepturi sint occaecati cupiditate non provident, similique sunt in culpa qui officia deserunt mollitia animi, id est laborum et dolorum fuga. Et harum quidem rerum facilis est et expedita distinctio. Nam libero tempore, cum soluta nobis est eligendi optio cumque nihil impedit quo minus id quod maxime placeat facere possimus, omnis voluptas assumenda est, omnis dolor repellendus. Temporibus autem quibusdam et aut officiis debitis.</p>
  <a class="btn btn-outline about-btn">Read More</a>
</section>

<section class="services">
  <h2 class="section-title serif" style="top:46px">Our Services</h2>
  <span class="title-rule" style="top:114px"></span>
  <div class="service" style="left:128px">
    <div class="photo" role="img" aria-label="Business handshake over a table" style="background:linear-gradient(135deg,#e8e4df 0%,#8d8a86 45%,#2a2a2c 100%)"></div>
    <h3>Honest</h3>
    <p>At vero eos et accusamus et iusto odio digni Tssimos culpa qui officia deserunt Nam libero tempore, cum soluta nobis est.</p>
    <a class="btn btn-outline">Read More</a>
  </div>
  <div class="service" style="left:448px">
    <div class="photo" role="img" aria-label="Smiling woman holding a tablet in an office" style="background:linear-gradient(160deg,#d9dfe3 0%,#8ea0ad 45%,#5a6a74 100%)"></div>
    <h3>Human</h3>
    <p>At vero eos et accusamus et iusto odio digni Tssimos culpa qui officia deserunt Nam libero tempore, cum soluta nobis est.</p>
    <a class="btn btn-outline">Read More</a>
  </div>
  <div class="service" style="left:768px">
    <div class="photo" role="img" aria-label="Team joining hands in a circle, seen from above" style="background:radial-gradient(circle at 50% 50%,#8a8480 0%,#9a9995 45%,#b5b4b1 100%)"></div>
    <h3>Trusting</h3>
    <p>At vero eos et accusamus et iusto odio digni Tssimos culpa qui officia deserunt Nam libero tempore, cum soluta nobis est.</p>
    <a class="btn btn-outline">Read More</a>
  </div>
</section>

<section class="events">
  <div class="event-box">
    <div class="event-photo" role="img" aria-label="Hand with glowing digital chart" style="background:linear-gradient(135deg,#0f3a3a 0%,#2f6a6a 50%,#cfd8d6 75%,#1d3b3d 100%)"></div>
    <div class="event-info" style="background:var(--red)">
      <h3>Upcoming Online Programs</h3>
      <h4>AT VERO EOS ET ACCUSA</h4>
      <p>March – April 2022<br>Program over 5 Sessions<br>March 7, 14, 21, 28 and April 4<br>18:00 – 21:00 CET</p>
      <a class="btn btn-white">Read More</a>
    </div>
    <div class="event-photo" role="img" aria-label="Smartphone with social reactions beside a laptop" style="background:linear-gradient(135deg,#6a4b3a 0%,#8e9fb8 45%,#c9ced6 70%,#3e3e42 100%)"></div>
    <div class="event-info" style="background:var(--ink)">
      <h3>Upcoming Webinars</h3>
      <h4>AT VERO EOS ET ACCUSA</h4>
      <p>March – April 2022<br>Program over 5 Sessions<br>March 7, 14, 21, 28 and April 4<br>18:00 – 21:00 CET</p>
      <a class="btn btn-white">Read More</a>
    </div>
  </div>
</section>

<section class="tiger">
  <div class="photo tiger-art" role="img" aria-label="Black and white tiger"></div>
  <span class="tiger-rule" style="top:130px"></span>
  <h2 class="tiger-title serif">We awaken<br>the tiger in you!</h2>
  <span class="tiger-rule" style="top:314px"></span>
</section>

<section class="blog">
  <h2 class="section-title serif" style="top:36px">Latest Blog</h2>
  <div class="photo blog-photo" role="img" aria-label="Man in glasses working on a laptop"></div>
  <article class="post" style="top:166px"><time>26 Feb 2022</time><h3>At vero eos et accusamus et iusto odio</h3><p>On the other hand, we denounce with righteous indignation and dislike men who are so beguiled and demoralized by the charms of pleasure of the moment, so blinded by desire.</p></article>
  <span class="post-rule" style="top:288px"></span>
  <article class="post" style="top:322px"><time>26 Feb 2022</time><h3>On the other hand, we denounce with</h3><p>On the other hand, we denounce with righteous indignation and dislike men who are so beguiled and demoralized by the charms of pleasure of the moment, so blinded by desire.</p></article>
  <span class="post-rule" style="top:448px"></span>
  <article class="post" style="top:482px"><time>26 Feb 2022</time><h3>Lorem ipsum dolor sit amet consectetur</h3><p>On the other hand, we denounce with righteous indignation and dislike men who are so beguiled and demoralized by the charms of pleasure of the moment, so blinded by desire.</p></article>
</section>

<section class="advantage">
  <p class="abs eyebrow">OUR ADVANTAGE</p>
  <h2 class="abs serif adv-title">A Community<br>Centered Around<br>Growth</h2>
  <p class="abs adv-text">On the other hand, we denounce with righteous indignation and dislike men who are so beguiled and demoralized by the charms of pleasure of the moment, so blinded by desire, that they cannot</p>
  <a class="btn btn-outline adv-btn">Read More</a>
  <div class="photo adv-photo" role="img" aria-label="Man presenting at a whiteboard" style="left:532px;width:174px;background:linear-gradient(180deg,#ece8e2 0%,#b8b2aa 50%,#6f6a66 100%)"></div>
  <div class="photo adv-photo" role="img" aria-label="Colleagues discussing documents" style="left:714px;width:172px;background:linear-gradient(180deg,#d6c9bc 0%,#8a6f5c 50%,#3a2e28 100%)"></div>
  <div class="photo adv-photo" role="img" aria-label="Team members reviewing work together" style="left:894px;width:174px;background:linear-gradient(180deg,#e4e2df 0%,#8b8682 50%,#3c3a3a 100%)"></div>
</section>

<section class="cta" role="img" aria-label="Dimmed background of a video call on a laptop">
  <h2 class="serif">READY TO MAKE BIG HAPPEN?</h2>
  <p>On the other hand, we denounce with righteous indignation and dislike men who are so beguiled and demoralized by the charms of pleasure of the moment, so blinded by desire.</p>
  <a class="btn btn-red cta-btn">Contact Me</a>
</section>

<footer class="site-footer">
  <div class="footer-brand">Lukas Brandstetter</div>
  <nav class="footer-nav"><span>About Us</span><span>Solutions</span><span>Courses &amp; Services</span><span>Events</span><span>Contact Us</span></nav>
  <div class="follow"><span>Follow us</span><span class="social"></span><span class="social"></span><span class="social"></span></div>
  <p class="copy">Copyright © 2022 All Rights Reserved</p>
</footer>

</body>
</html>
```